Marlow Fields Thank-You Tag

Looking for a file that incorporates current branding/colors and says:

"Thanks for Swimming with Us!"
Marlow Fields Otters

Samples of other pieces we've done recently are attached.

Will be printed on cardstock that is
Width: 3.5 inches
Height: 2.5 inches

```html
<!DOCTYPE html>
<html lang="en">
<head>
<meta charset="utf-8">
<title>Marlow Fields Thank-You Tag</title>
<link rel="stylesheet" href="https://fonts.googleapis.com/css2?family=Anton&family=Montserrat:wght@800&display=swap">
<style>
  :root {
    --surround: #b7b7b7;
    --pool-blue: #2b51a2;
    --light-blue: #8abbe6;
    --splash-pink: #ef62a2;
    --white: #ffffff;
    --ink: #000000;
    --silver: #b9bcc4;
  }
  html, body {
    margin: 0;
    padding: 0;
    width: 1200px;
    height: 906px;
    overflow: hidden;
    background: var(--surround);
  }
  .tag {
    position: absolute;
    left: 113px;
    top: 102px;
    width: 974px;
    height: 699px;
    background: var(--pool-blue);
    overflow: hidden;
  }
  .year-digit {
    position: absolute;
    margin: 0;
    font-family: "Montserrat", sans-serif;
    font-weight: 800;
    font-size: 192px;
    line-height: 1;
  }
  .year-digit--two-top { left: 82px; top: 124px; color: var(--white); }
  .year-digit--two-low { left: 128px; top: 250px; color: var(--splash-pink); }
  .year-digit--six { left: 210px; top: 298px; color: var(--splash-pink); }
  .year-ring {
    position: absolute;
    left: 206px;
    top: 166px;
    width: 130px;
    height: 130px;
  }
  .club-name {
    position: absolute;
    left: 226px;
    top: 208px;
    width: 90px;
    margin: 0;
    text-align: center;
    font-family: "Anton", sans-serif;
    font-size: 13px;
    line-height: 1.15;
    letter-spacing: 1px;
    color: var(--white);
    text-transform: uppercase;
  }
  .headline {
    position: absolute;
    margin: 0;
    font-family: "Anton", sans-serif;
    font-weight: 400;
    text-transform: uppercase;
    line-height: 1;
    white-space: nowrap;
  }
  .headline--thanks {
    left: 554px;
    top: 188px;
    font-size: 62px;
    letter-spacing: 2px;
    color: var(--white);
    transform: rotate(1deg);
    transform-origin: left top;
  }
  .swim-banner {
    position: absolute;
    left: 446px;
    top: 258px;
    width: 464px;
    height: 104px;
    background: var(--splash-pink);
    border-radius: 8px;
    transform: rotate(2deg);
  }
  .headline--swimming {
    left: 462px;
    top: 256px;
    font-size: 104px;
    color: var(--ink);
    -webkit-text-stroke: 4px var(--white);
    paint-order: stroke fill;
    transform: rotate(2.5deg);
    transform-origin: left top;
  }
  .headline--with-us {
    left: 550px;
    top: 364px;
    font-size: 60px;
    letter-spacing: 2px;
    color: var(--splash-pink);
    transform: rotate(2deg);
    transform-origin: left top;
  }
  .art {
    position: absolute;
    border-radius: 50%;
  }
  .art--leaping-silver { left: 444px; top: 92px; width: 108px; height: 120px; background: var(--silver); opacity: .85; }
  .art--splash-pink { left: 452px; top: 166px; width: 90px; height: 78px; background: var(--splash-pink); }
  .art--leaping-white { left: 662px; top: 452px; width: 104px; height: 100px; background: var(--white); opacity: .9; }
  .art--splash-white { left: 854px; top: 482px; width: 48px; height: 42px; background: var(--white); }
  .waves {
    position: absolute;
    left: 0;
    bottom: 0;
    width: 974px;
    height: 170px;
  }
</style>
</head>
<body>
  <main class="tag">
    <p class="year-digit year-digit--two-top">2</p>
    <svg class="year-ring" viewBox="0 0 130 130" aria-hidden="true">
      <circle cx="65" cy="65" r="53" fill="none" stroke="var(--white)" stroke-width="24"/>
    </svg>
    <p class="club-name">Marlow<br>Fields<br>Otters</p>
    <p class="year-digit year-digit--two-low">2</p>
    <p class="year-digit year-digit--six">6</p>

    <div class="art art--leaping-silver" role="img" aria-label="Silver leaping dolphin illustration"></div>
    <div class="art art--splash-pink" role="img" aria-label="Pink water splash illustration"></div>

    <h1 class="headline headline--thanks">Thanks for</h1>
    <div class="swim-banner"></div>
    <p class="headline headline--swimming">Swimming</p>
    <p class="headline headline--with-us">With us!</p>

    <svg class="waves" viewBox="0 0 974 170" preserveAspectRatio="none" aria-hidden="true">
      <path fill="var(--white)" d="M0,28 Q70,4 140,28 T280,28 T420,28 T560,28 T700,28 T840,28 T980,28 V170 H0 Z"/>
      <path fill="var(--light-blue)" d="M0,48 Q70,24 140,48 T280,48 T420,48 T560,48 T700,48 T840,48 T980,48 V170 H0 Z"/>
      <path fill="var(--white)" d="M0,70 Q70,46 140,70 T280,70 T420,70 T560,70 T700,70 T840,70 T980,70 V170 H0 Z"/>
      <path fill="var(--splash-pink)" d="M0,84 Q70,60 140,84 T280,84 T420,84 T560,84 T700,84 T840,84 T980,84 V170 H0 Z"/>
    </svg>

    <div class="art art--leaping-white" role="img" aria-label="White dolphin diving into the waves illustration"></div>
    <div class="art art--splash-white" role="img" aria-label="White water splash illustration"></div>
  </main>
</body>
</html>
```